Wealth Management Business Card

We are a professional services consulting firm that specializes in high net worth individuals over $25,000,000, executives C-suite and above, closely held businesses owners, family offices and highly compensated employees.

Our focus is on risk mitigation and tax efficient strategies. Our clients take their risk on themselves and have a proven track record generating wealth. Our directive is to preserve and protect the wealth they’ve already created.

Our company Harbridge Advisory is geared around five directives of asset protection:
1) Legal Structuring
2) Leverage & Financing
3) Risk Management - Asset Protection & Insurance, Trustee Work
4) Asset Management & Investing - Under www.qelvantcapital.com
5) Tax Efficient Strategies

Our Company Mark is a Pentagon with a key in the middle. A pentagon is the most efficient defensive structure. Each point of a pentagon is equal distance front every point . Each side provides support to another and works together, which is the key to our clients success.

Our key colors are blue, black and silver.

We ‘re located in the Pacific Northwest with bi coastal and international clients. We have fewer, higher net worth clients and provide exceptional customer service. We do not do social media.

website is www.harbridgepath.com

Target Market(s)

High End Clients

Contact Information for Business Card

extra thick

Font styles to use
Serif

Requirements
Must have
• Metalic foil for lettering.
Black Background on one side
White Background on the other
Horizontal Format Only
No Rounded corners
Not Marketing sales information on the card.
Nice to have
• imprinted texture on the card
Should not have
• lots of color

```html
<!DOCTYPE html>
<html lang="en">
<head>
<meta charset="utf-8">
<title>Harbridge Advisory – Business Card</title>
<link rel="stylesheet" href="https://fonts.googleapis.com/css2?family=Cinzel:wght@600&family=Arimo:wght@400&display=swap">
<style>
  :root {
    --backdrop: #d9dadc;
    --card-black: #070708;
    --card-black-glow: #1b1b1e;
    --card-white: #eeeff1;
    --card-white-band: #e2e3e6;
    --navy: #1f3170;
    --accent-blue: #2f86d8;
    --ink: #1a1a1a;
    --shadow: rgba(0, 0, 0, 0.28);
  }
  * { box-sizing: border-box; margin: 0; padding: 0; }
  html, body {
    width: 1200px;
    height: 800px;
    overflow: hidden;
    background: var(--backdrop);
  }
  .canvas {
    width: 1200px;
    height: 800px;
    display: flex;
    align-items: center;
    justify-content: center;
    gap: 60px;
  }
  .card {
    position: relative;
    width: 525px;
    height: 300px;
    overflow: hidden;
    box-shadow: 0 14px 30px var(--shadow);
  }

  /* Black side */
  .card--back {
    background: radial-gradient(ellipse at 75% 10%, var(--card-black-glow) 0%, var(--card-black) 60%);
    display: flex;
    flex-direction: column;
    align-items: center;
    justify-content: center;
    gap: 38px;
  }
  .brand {
    display: flex;
    align-items: center;
    gap: 14px;
  }
  .brand__mark {
    width: 14px;
    height: 14px;
    background: var(--accent-blue);
  }
  .brand__name {
    font-family: "Cinzel", Georgia, serif;
    font-weight: 600;
    font-size: 26px;
    letter-spacing: 2px;
    line-height: 1.15;
    color: var(--navy);
  }
  .card--back .brand__name { color: var(--accent-blue); }
  .contact {
    list-style: none;
    display: grid;
    grid-template-columns: auto auto;
    gap: 10px 34px;
    font-family: "Arimo", Arial, sans-serif;
    font-size: 12.5px;
    color: var(--accent-blue);
  }
  .contact__item {
    display: flex;
    align-items: center;
    gap: 7px;
  }
  .contact__icon {
    width: 12px;
    height: 12px;
    fill: var(--accent-blue);
    flex: none;
  }

  /* White side */
  .card--front {
    background: var(--card-white);
  }
  .card--front .band {
    position: absolute;
    top: 0;
    right: 0;
    width: 260px;
    height: 100%;
    background: linear-gradient(160deg, var(--card-white-band) 0%, var(--card-white) 85%);
  }
  .card--front .brand {
    position: absolute;
    left: 40px;
    top: 172px;
  }
  .card--front .brand__name { font-size: 24px; }
  .directives {
    position: absolute;
    left: 300px;
    top: 78px;
    list-style: none;
    font-family: "Arimo", Arial, sans-serif;
    font-size: 13px;
    color: var(--ink);
  }
  .directives__item {
    display: flex;
    align-items: center;
    gap: 6px;
    margin-bottom: 12px;
  }
  .directives__item::before {
    content: "";
    width: 5px;
    height: 5px;
    border-radius: 50%;
    background: var(--ink);
  }
  .directives__item:nth-child(2) { margin-left: 8px; }
  .directives__item:nth-child(3) { margin-left: 16px; }
  .directives__item:nth-child(4) { margin-left: 24px; }
  .directives__item:nth-child(5) { margin-left: 32px; }
</style>
</head>
<body>
<main class="canvas">
  <section class="card card--back" aria-label="Card back">
    <div class="brand">
      <span class="brand__mark"></span>
      <span class="brand__name">Harbridge<br>Advisory</span>
    </div>
    <ul class="contact">
      <li class="contact__item">
        <svg class="contact__icon" viewBox="0 0 12 12"><path d="M6 0a4 4 0 0 0-4 4c0 3 4 8 4 8s4-5 4-8a4 4 0 0 0-4-4zm0 5.6A1.6 1.6 0 1 1 6 2.4a1.6 1.6 0 0 1 0 3.2z"/></svg>
        1420 Alder Ave, Suite 300
      </li>
      <li class="contact__item">
        <svg class="contact__icon" viewBox="0 0 12 12"><path d="M0 2h12v8H0z" opacity=".35"/><path d="M0 2l6 4 6-4v1.3L6 7.3 0 3.3z"/></svg>
        info@harbridgepath.com
      </li>
      <li class="contact__item">
        <svg class="contact__icon" viewBox="0 0 12 12"><path d="M2.4 0.5l2 2.6-1.2 1.5c.8 1.6 2.1 2.9 3.7 3.7l1.5-1.2 2.6 2-1.2 2.1C5.3 11 1 6.7.3 1.7z"/></svg>
        (503) 555-0147
      </li>
      <li class="contact__item">
        <svg class="contact__icon" viewBox="0 0 12 12"><circle cx="6" cy="6" r="5.2" fill="none" stroke="currentColor" stroke-width="1.2" style="stroke:var(--accent-blue)"/><path d="M1 6h10M6 .8c-2.6 3-2.6 7.4 0 10.4M6 .8c2.6 3 2.6 7.4 0 10.4" fill="none" style="stroke:var(--accent-blue)" stroke-width="1"/></svg>
        www.harbridgepath.com
      </li>
    </ul>
  </section>

  <section class="card card--front" aria-label="Card front">
    <div class="band" role="img" aria-label="Soft silver decorative band"></div>
    <div class="brand">
      <span class="brand__mark"></span>
      <span class="brand__name">Harbridge<br>Advisory</span>
    </div>
    <ul class="directives">
      <li class="directives__item">Legal Structuring</li>
      <li class="directives__item">Leverage &amp; Financing</li>
      <li class="directives__item">Risk Management</li>
      <li class="directives__item">Asset Management &amp; Investing</li>
      <li class="directives__item">Tax Efficient Strategies</li>
    </ul>
  </section>
</main>
</body>
</html>
```